Business card design needed

Family General Practitioner/ Family Physician.
Logo is the logo of the Crestmoor Guild of Family Clinicians Australia
http://kvplm.tarevo.edu.au/PictureGallery/logos/pages/CGFC%20logo_jpg.htm

Reason: Just a bit more time to make changes and the weekend for me to look at things closely and to choose. Thanks, Lumi

Thanks for all the submissions. So many of them are really works of art. Not one of them are not good. The ones that I am eliminating are the ones that I think are not suitable for me personally only, and because if I don't, it makes it very difficult to decide as many of you are also sending me slight variations of a card. I have just decided to choose a second place card too. Can't thank you all enough. Good luck, Lumi. P.S - Working today till 10 pm as the card says :-), so probably won't be able to give a feedback till late Saturday night or Sunday morning here in Sydney, Australia. 

Reason: Just added a second place to the budget and realised that Australia is ahead of the rest of the world in the time zone (only :-) - don't want to offend anyone or start a debate!! ) , so Monday deadline will mean it will be a weekend for the rest of the world. Just wanted to give everyone more time to submit their best, especially since I will be picking a second card too. Can't thank everyone enough for the submissions. P.S - Not keen on photos on the card.

Contact Information for Business Card

Dr. Lumi Harcourt M.B.B.S., F.C.G.F.C
Family General Practitioner
Address, timings, phone and fax number on the back.

Requirements
Must have
• Timings
Mon 7 am - 7 pm
Tues 7 am - 12 pm
Wed 7 am - 10 pm
Thurs 7 am - 12 pm
Fri 7 am - 8 pm
Sat 8 am - 10 pm
Sun - Off

```html
<!DOCTYPE html>
<html lang="en">
<head>
<meta charset="utf-8">
<title>Dr. Lumi Harcourt – Business Card</title>
<link rel="stylesheet" href="https://fonts.googleapis.com/css2?family=Oswald:wght@400;500;600;700&display=swap">
<style>
  :root {
    --page: #ecebe7;
    --card-white: #ffffff;
    --sky: #1ba9d6;
    --sky-deep: #0b8fc2;
    --sky-light: #5cc7e6;
    --teal-soft: #7fd0d8;
    --leaf: #a9c96a;
    --leaf-deep: #8fb94e;
    --ink: #111111;
    --paper-blue: #b4dde2;
    --text-dark: #0d5f7e;
    --text-light: #ffffff;
  }
  * { margin: 0; padding: 0; box-sizing: border-box; }
  html, body { width: 1200px; height: 960px; overflow: hidden; }
  body {
    background: var(--page);
    font-family: "Oswald", "Arial Narrow", sans-serif;
    position: relative;
  }
  .card {
    position: absolute;
    left: 250px;
    width: 700px;
    height: 400px;
    overflow: hidden;
    box-shadow: 0 6px 18px rgba(0,0,0,.18);
  }
  .card--front { top: 40px; background: var(--sky); }
  .card--back { top: 500px; background: var(--paper-blue); }

  .card__art { position: absolute; inset: 0; }

  .guild-mark {
    position: absolute;
    top: 30px;
    right: 44px;
    display: flex;
    align-items: center;
    gap: 10px;
    color: var(--sky-deep);
    font-weight: 600;
    font-size: 30px;
    letter-spacing: 2px;
  }
  .guild-mark__dot {
    width: 28px; height: 28px;
    border-radius: 50%;
    background: var(--sky-deep);
  }

  .identity {
    position: absolute;
    right: 0;
    top: 124px;
    width: 380px;
  }
  .identity__credentials {
    color: var(--text-light);
    font-weight: 600;
    font-size: 17px;
    letter-spacing: 1.5px;
    padding-left: 14px;
    margin-bottom: 4px;
  }
  .identity__name {
    background: var(--ink);
    color: var(--text-light);
    font-weight: 700;
    font-size: 36px;
    line-height: 1;
    padding: 6px 14px 8px;
  }
  .identity__role {
    color: var(--text-light);
    font-weight: 500;
    font-size: 20px;
    letter-spacing: 1px;
    padding-left: 14px;
    margin-top: 6px;
  }

  .hours {
    position: absolute;
    left: 0; top: 0; bottom: 0;
    width: 330px;
    background: linear-gradient(160deg, var(--sky) 0%, var(--sky-deep) 100%);
    padding: 44px 0 0 44px;
    color: var(--text-light);
  }
  .hours__title {
    font-weight: 600;
    font-size: 22px;
    letter-spacing: 2px;
    margin-bottom: 14px;
  }
  .hours__list { list-style: none; }
  .hours__row {
    display: flex;
    font-size: 18px;
    line-height: 1.7;
  }
  .hours__day { width: 70px; font-weight: 600; }

  .contact {
    position: absolute;
    left: 330px; top: 0; right: 0; bottom: 0;
    padding: 44px 40px 0 44px;
    color: var(--text-dark);
  }
  .contact__title {
    font-weight: 600;
    font-size: 22px;
    letter-spacing: 2px;
    margin-bottom: 14px;
  }
  .contact__address {
    font-style: normal;
    font-size: 18px;
    line-height: 1.7;
    margin-bottom: 24px;
  }
  .contact__list { list-style: none; }
  .contact__row {
    display: flex;
    align-items: center;
    font-size: 18px;
    line-height: 1.9;
  }
  .contact__label { width: 70px; font-weight: 600; }
  .contact__strip {
    position: absolute;
    left: 0; right: 0; bottom: 0;
    height: 60px;
    background: linear-gradient(90deg, var(--leaf) 0%, var(--sky-light) 55%, var(--sky) 100%);
  }
</style>
</head>
<body>

  <section class="card card--front">
    <svg class="card__art" viewBox="0 0 700 400" width="700" height="400">
      <defs>
        <linearGradient id="sky-band" x1="0" y1="0" x2="1" y2="1">
          <stop offset="0" stop-color="#1ba9d6"/>
          <stop offset="1" stop-color="#0b8fc2"/>
        </linearGradient>
        <linearGradient id="faint-tiles" x1="0" y1="0" x2="1" y2="0">
          <stop offset="0" stop-color="#7fd0d8"/>
          <stop offset="1" stop-color="#2fb3dc"/>
        </linearGradient>
        <linearGradient id="tile-field" x1="0" y1="1" x2="1" y2="0">
          <stop offset="0" stop-color="#8fb94e"/>
          <stop offset="0.3" stop-color="#a9c96a"/>
          <stop offset="0.55" stop-color="#5cc7e6"/>
          <stop offset="0.8" stop-color="#1ba9d6"/>
          <stop offset="1" stop-color="#a9c96a"/>
        </linearGradient>
      </defs>
      <rect width="700" height="400" fill="url(#sky-band)"/>
      <path d="M0 40 Q250 160 430 150 L430 240 L0 240 Z" fill="url(#faint-tiles)" opacity=".55"
            role="img" aria-label="Faint pattern of light teal rounded tiles"/>
      <path d="M400 0 H700 V118 Q540 118 400 0 Z" fill="#ffffff"/>
      <path d="M0 150 Q200 250 430 250 L700 250 V400 H0 Z" fill="url(#tile-field)"
            role="img" aria-label="Decorative pattern of interlocking rounded green and blue tiles"/>
      <path d="M0 150 Q200 250 430 250 L700 250" fill="none" stroke="#ffffff" stroke-width="4" opacity=".85"/>
    </svg>

    <div class="guild-mark">
      <span class="guild-mark__dot"></span>
      <span>CGFC</span>
    </div>

    <div class="identity">
      <p class="identity__credentials">M.B.B.S. F.C.G.F.C</p>
      <h1 class="identity__name">Dr. Lumi Harcourt</h1>
      <p class="identity__role">FAMILY GENERAL PRACTITIONER</p>
    </div>
  </section>

  <section class="card card--back">
    <div class="hours">
      <h2 class="hours__title">OPENING HOURS</h2>
      <ul class="hours__list">
        <li class="hours__row"><span class="hours__day">Mon</span><span>7 am – 7 pm</span></li>
        <li class="hours__row"><span class="hours__day">Tues</span><span>7 am – 12 pm</span></li>
        <li class="hours__row"><span class="hours__day">Wed</span><span>7 am – 10 pm</span></li>
        <li class="hours__row"><span class="hours__day">Thurs</span><span>7 am – 12 pm</span></li>
        <li class="hours__row"><span class="hours__day">Fri</span><span>7 am – 8 pm</span></li>
        <li class="hours__row"><span class="hours__day">Sat</span><span>8 am – 10 pm</span></li>
        <li class="hours__row"><span class="hours__day">Sun</span><span>Off</span></li>
      </ul>
    </div>

    <div class="contact">
      <h2 class="contact__title">CONTACT</h2>
      <address class="contact__address">
        Suite 4, 18 Wattlebrook Road<br>
        Kellerton NSW 2150
      </address>
      <ul class="contact__list">
        <li class="contact__row"><span class="contact__label">Phone</span><span>(02) 5550 1842</span></li>
        <li class="contact__row"><span class="contact__label">Fax</span><span>(02) 5550 1843</span></li>
      </ul>
    </div>
    <div class="contact__strip" style="left:330px" role="img" aria-label="Narrow band of green and blue tile pattern"></div>
  </section>

</body>
</html>
```